Develop a Corporate Identity for Quomentrix.

I am starting a personal website for business and financial advice. I am using the wordpress 2013 theme. Develop a range of brand items i.e. logos, banners, header images etc for the website and social media e.g. facebook, twitter, google+, etc. based on the information at http://www.quomentrix.example/

```html
<!DOCTYPE html>
<html lang="en">
<head>
<meta charset="utf-8">
<title>Quomentrix — Corporate Identity</title>
<link rel="stylesheet" href="https://fonts.googleapis.com/css2?family=Questrial&display=swap">
<style>
  :root {
    --teal: #12918a;
    --charcoal: #4a4a4a;
    --mist: #eeeeee;
    --paper: #ffffff;
    --edge: #d6d6d6;
  }
  html, body {
    margin: 0;
    padding: 0;
    overflow: hidden;
    background: var(--paper);
  }
  .canvas {
    position: relative;
    width: 1200px;
    height: 800px;
    overflow: hidden;
    background: var(--paper);
    font-family: "Questrial", "Century Gothic", sans-serif;
    color: var(--charcoal);
  }

  /* Wordmark: plain name with one circle */
  .wordmark {
    position: absolute;
    display: flex;
    align-items: center;
  }
  .wordmark__dot {
    border-radius: 50%;
    background: var(--teal);
    flex: none;
  }
  .wordmark__name {
    color: var(--charcoal);
    letter-spacing: 0.02em;
    line-height: 1;
    white-space: nowrap;
  }

  .wordmark--primary { left: 83px; top: 62px; gap: 14px; }
  .wordmark--primary .wordmark__dot { width: 54px; height: 54px; }
  .wordmark--primary .wordmark__name { font-size: 56px; }

  .wordmark--card { left: 107px; top: 512px; gap: 8px; }
  .wordmark--card .wordmark__dot { width: 22px; height: 22px; }
  .wordmark--card .wordmark__name { font-size: 22px; }

  .wordmark--letter { left: 628px; top: 68px; gap: 8px; }
  .wordmark--letter .wordmark__dot { width: 22px; height: 22px; }
  .wordmark--letter .wordmark__name { font-size: 22px; }

  /* Business card front */
  .card-front {
    position: absolute;
    left: 71px; top: 220px;
    width: 380px; height: 217px;
    background: var(--teal);
    display: flex;
    align-items: center;
    justify-content: center;
  }
  .card-front__stripe {
    position: absolute;
    right: 0; top: 0;
    width: 15px; height: 100%;
    background: var(--charcoal);
  }
  .card-front__name {
    color: var(--paper);
    font-size: 30px;
    letter-spacing: 0.04em;
    margin-right: 15px;
  }

  /* Business card back */
  .card-back {
    position: absolute;
    left: 71px; top: 483px;
    width: 380px; height: 218px;
    background: var(--paper);
    overflow: hidden;
  }
  .card-back__stripe {
    position: absolute;
    left: 0; top: 0;
    width: 15px; height: 100%;
    background: var(--charcoal);
  }
  .card-back__motif {
    position: absolute;
    left: 110px; top: 20px;
    width: 300px; height: 300px;
    border-radius: 50%;
    background: var(--mist);
  }

  /* Letterhead */
  .letterhead {
    position: absolute;
    left: 593px; top: 36px;
    width: 531px; height: 712px;
    background: var(--paper);
    box-shadow: 0 0 0 1px var(--edge);
    overflow: hidden;
  }
  .letterhead__stripe {
    position: absolute;
    left: 0; top: 0;
    width: 13px; height: 100%;
    background: var(--teal);
  }
  .letterhead__motif {
    position: absolute;
    left: 220px; top: 312px;
    width: 440px; height: 440px;
    border-radius: 50%;
    background: var(--mist);
  }

  /* Contact text */
  .contact {
    position: absolute;
    margin: 0;
    text-align: right;
    font-size: 8px;
    line-height: 13px;
    letter-spacing: 0.04em;
    text-transform: uppercase;
    color: var(--charcoal);
    font-style: normal;
  }
  .contact strong { font-weight: 700; }
  .contact--letter { right: 36px; top: 26px; }
  .contact--card-top { right: 28px; top: 22px; }
  .contact--card-bottom { right: 28px; top: 120px; }
</style>
</head>
<body>
<main class="canvas">

  <div class="wordmark wordmark--primary">
    <span class="wordmark__dot"></span>
    <span class="wordmark__name">QUOMENTRIX</span>
  </div>

  <section class="card-front" aria-label="Business card front">
    <span class="card-front__name">QUOMENTRIX</span>
    <div class="card-front__stripe"></div>
  </section>

  <section class="card-back" aria-label="Business card back">
    <div class="card-back__motif"></div>
    <div class="card-back__stripe"></div>
    <address class="contact contact--card-top">
      Dana Morel<br><strong>Advisor</strong>
    </address>
    <address class="contact contact--card-bottom">
      Head Office<br>
      14 Larkfield Row, Suite 3<br>
      +00 123 456 7890<br>
      quomentrix.example
    </address>
  </section>

  <div class="wordmark wordmark--card">
    <span class="wordmark__dot"></span>
    <span class="wordmark__name">QUOMENTRIX</span>
  </div>

  <section class="letterhead" aria-label="Letterhead">
    <div class="letterhead__motif"></div>
    <div class="letterhead__stripe"></div>
    <address class="contact contact--letter">
      Head Office<br>
      14 Larkfield Row, Suite 3<br>
      +00 123 456 7890<br>
      hello@quomentrix.example
    </address>
  </section>

  <div class="wordmark wordmark--letter">
    <span class="wordmark__dot"></span>
    <span class="wordmark__name">QUOMENTRIX</span>
  </div>

</main>
</body>
</html>
```